CBD AgriBusiness Verdant Laurel Business Card

We are HiTec producer of medical cannabis CBD Switzerland of high quality. Our website is morvelta.com, we will also revisit it graphically, the winner of this contest will be the graphic designer chosen for the new design of the website. We stand out by the skill of the team, many of our engineers we win laurel verdant. I join the current map to take as an example but to revisit completely: deletion of surname and first name, modification of funds (front / back), reorganization of text info, highlighting the address of the website. three characteristics define the business card: Professional, Class, refined. The business card must be optimized for soft-touch and selective varnish printing.
Updates

Besoin de plus de jours pour examiner

Target Market(s)

Customers and Suppliers

Industry/Entity Type

Agribusiness

Contact Information for Business Card

Logo, Tél / Whatsapp, mail, url du site : morvelta.com

Font styles to use
Sans Serif

Requirements
Must have
• Logo of morvelta.com
Nice to have
• a design that stands out well on the selective varnish
Should not have
• Last name and first name

```html
<!DOCTYPE html>
<html lang="en">
<head>
<meta charset="utf-8">
<title>Morvelta Business Card</title>
<link rel="stylesheet" href="https://fonts.googleapis.com/css2?family=Work+Sans:wght@400;500;700&display=swap">
<style>
  :root {
    --page: #e6e7e8;
    --card-white: #ffffff;
    --card-fade: #eeeeee;
    --charcoal: #48494b;
    --charcoal-deep: #3d3e40;
    --ink: #454648;
    --leaf: #72b84a;
    --logo-light: #bfc0c2;
  }
  * { box-sizing: border-box; margin: 0; padding: 0; }
  html, body { width: 1200px; height: 900px; overflow: hidden; }
  body {
    background: var(--page);
    font-family: "Work Sans", sans-serif;
    display: flex;
    flex-direction: column;
    align-items: center;
    justify-content: center;
    gap: 60px;
  }
  .card {
    position: relative;
    width: 560px;
    height: 320px;
    border-radius: 18px;
    overflow: hidden;
    box-shadow: 0 10px 28px rgba(0,0,0,0.18);
  }
  .card-front {
    background: radial-gradient(ellipse at 60% 45%, var(--card-white) 40%, var(--card-fade) 100%);
  }
  .brand { display: flex; align-items: center; gap: 8px; }
  .brand-mark { width: 22px; height: 22px; background: var(--leaf); }
  .brand-name { font-weight: 700; letter-spacing: -0.5px; }
  .card-front .brand { position: absolute; left: 32px; top: 34px; }
  .card-front .brand-name { font-size: 38px; color: var(--ink); }
  .divider {
    position: absolute;
    left: 44px;
    right: 80px;
    top: 140px;
    height: 1.5px;
    background: var(--leaf);
  }
  .contacts {
    position: absolute;
    left: 26px;
    top: 166px;
    list-style: none;
    font-size: 13px;
    color: var(--ink);
    line-height: 20px;
  }
  .contacts li { display: flex; align-items: center; gap: 8px; }
  .contacts svg { width: 10px; height: 10px; flex: none; }
  .contacts .site-accent { color: var(--leaf); }
  .address {
    position: absolute;
    right: 34px;
    top: 236px;
    text-align: right;
    font-size: 13px;
    color: var(--ink);
    line-height: 19px;
  }
  .base-band { position: absolute; left: 0; bottom: 0; width: 560px; height: 40px; }
  .card-back {
    background: linear-gradient(160deg, var(--charcoal) 0%, var(--charcoal-deep) 100%);
    display: flex;
    align-items: center;
    justify-content: center;
  }
  .card-back .brand { gap: 14px; }
  .card-back .brand-mark { width: 40px; height: 40px; }
  .card-back .brand-name { font-size: 72px; color: var(--logo-light); }
</style>
</head>
<body>
  <section class="card card-front">
    <div class="brand">
      <span class="brand-mark"></span>
      <span class="brand-name">morvelta</span>
    </div>
    <div class="divider"></div>
    <ul class="contacts">
      <li><svg viewBox="0 0 10 10"><path d="M2 1l2 2-1 1.2c.6 1.2 1.6 2.2 2.8 2.8L7 6l2 2-1.4 1.4C4.5 9 1 5.5.6 2.4z" fill="var(--leaf)"/></svg>+41 (0) 70 555 01 23</li>
      <li><svg viewBox="0 0 10 10"><rect x="2.5" y="0.5" width="5" height="9" rx="1" fill="none" stroke="var(--leaf)"/></svg>+44 7700 90 01 46</li>
      <li><svg viewBox="0 0 10 10"><rect x="0.5" y="2" width="9" height="6" fill="none" stroke="var(--leaf)"/><path d="M.5 2L5 5.5 9.5 2" fill="none" stroke="var(--leaf)"/></svg>office@morvelta.com</li>
      <li><svg viewBox="0 0 10 10"><circle cx="5" cy="5" r="4.5" fill="var(--leaf)"/></svg><span>www.<span class="site-accent">morvelta</span>.com</span></li>
    </ul>
    <p class="address">58b Harlow Lane,<br>Eastford, NZ, 4120</p>
    <svg class="base-band" viewBox="0 0 560 40" preserveAspectRatio="none">
      <path d="M0 33 L220 33 Q232 33 238 40 L0 40 Z" fill="var(--leaf)"/>
      <path d="M0 37 L230 37 Q250 37 258 28 Q264 22 280 22 L560 22 L560 40 L0 40 Z" fill="var(--charcoal)"/>
    </svg>
  </section>

  <section class="card card-back">
    <div class="brand">
      <span class="brand-mark"></span>
      <span class="brand-name">morvelta</span>
    </div>
  </section>
</body>
</html>
```